Cover for Inspirational Daily Journal

This is the cover for a daily journal that will focus on inspirational content for black women. The cover should have a picture or silhouette of a black woman with a crown. The title is: "Born to Bloom: A Year of Bright Mornings." The back won't have any words. Also the journal will be published on Penwick.

```html
<!DOCTYPE html>
<html lang="en">
<head>
<meta charset="utf-8">
<title>Born to Bloom: A Year of Bright Mornings</title>
<link href="https://fonts.googleapis.com/css2?family=Oswald:wght@500;600&display=swap" rel="stylesheet">
<style>
  :root {
    --paper: #f7f3ee;
    --title-red: #de4b27;
    --ink: #1d1d1b;
    --crown-gold: #e9b424;
    --skin-brown: #7a2e14;
    --shirt-red: #d9482a;
  }
  html, body {
    margin: 0;
    padding: 0;
    overflow: hidden;
    background: var(--paper);
  }
  .cover {
    position: relative;
    width: 846px;
    height: 1200px;
    overflow: hidden;
    background: var(--paper);
    font-family: "Oswald", "Arial Narrow", sans-serif;
  }
  .title-line {
    position: absolute;
    left: 0;
    width: 100%;
    margin: 0;
    text-align: center;
    text-transform: uppercase;
    line-height: 1;
    white-space: nowrap;
    font-weight: 600;
  }
  .title-top {
    top: 95px;
    font-size: 206px;
    color: var(--title-red);
    letter-spacing: -2px;
  }
  .title-main {
    top: 275px;
    font-size: 206px;
    color: var(--ink);
    letter-spacing: -1px;
  }
  .subtitle {
    top: 510px;
    font-size: 60px;
    font-weight: 500;
    color: var(--ink);
    letter-spacing: 0;
  }
  .portrait {
    position: absolute;
    left: 248px;
    top: 655px;
    width: 310px;
    height: 545px;
  }
</style>
</head>
<body>
  <main class="cover">
    <h1 class="title-line title-top">Born to</h1>
    <p class="title-line title-main">Bloom</p>
    <p class="title-line subtitle">A Year of Bright Mornings</p>
    <svg class="portrait" viewBox="0 0 310 545" role="img" aria-label="Illustration of a Black woman in profile, eyes closed, wearing a golden crown and a red top">
      <defs>
        <linearGradient id="portrait-tones" x1="0" y1="0" x2="0" y2="1">
          <stop offset="0" stop-color="var(--crown-gold)"/>
          <stop offset="0.18" stop-color="var(--ink)"/>
          <stop offset="0.55" stop-color="var(--skin-brown)"/>
          <stop offset="0.75" stop-color="var(--shirt-red)"/>
        </linearGradient>
      </defs>
      <rect x="0" y="0" width="310" height="545" rx="120" fill="url(#portrait-tones)"/>
    </svg>
  </main>
</body>
</html>
```